2 Creative Website Banners for Furniture Brand

Morning Tobrasca....
The get a great night sleep banner is complete - we are happy with that one.
Ive uploaded a slightly different concept for the other banner below. This is just something rough ive thrown together. But you can see I have added a curve, a maroon coloured background which is slightly transparent and a big heart in the background....
I do not necessarily want to use this heart image but something a bit like this (a nice graphic, gif etc) but something quite elegant faded in, or perhaps a number of hearts (done in a tasteful way). Also can we keep the typography in the same format as you can see for this one.
Nearly there :)!
Industry/Entity Type
Furniture

```html
<!DOCTYPE html>
<html lang="en">
<head>
<meta charset="utf-8">
<title>Find a Look You Love – Bedrooms Banner</title>
<link href="https://fonts.googleapis.com/css2?family=Great+Vibes&family=Josefin+Sans:wght@600&family=Cinzel:wght@600&family=Arimo&display=swap" rel="stylesheet">
<style>
  :root {
    --backdrop-light: #d2cdc5;
    --backdrop-mid: #bcb6ad;
    --backdrop-dark: #a8a197;
    --maroon-veil: rgba(118, 34, 52, 0.34);
    --heart-tint: #f4e6e8;
    --room-light: #8c8084;
    --room-mid: #665b60;
    --room-dark: #2b2527;
    --curve-edge: rgba(255, 255, 255, 0.55);
    --ink: #111010;
    --ink-soft: #2e2a29;
    --button-fill: #ece6dc;
  }
  html, body {
    margin: 0;
    padding: 0;
    overflow: hidden;
    background: #ffffff;
  }
  .banner {
    position: relative;
    width: 1200px;
    height: 356px;
    overflow: hidden;
  }
  .banner__art {
    position: absolute;
    inset: 0;
    width: 1200px;
    height: 356px;
    display: block;
  }
  .banner__content {
    position: absolute;
    inset: 0;
  }
  .headline-top {
    position: absolute;
    left: 200px;
    top: 52px;
    margin: 0;
    font-family: "Josefin Sans", sans-serif;
    font-weight: 600;
    font-size: 29px;
    letter-spacing: 6px;
    color: var(--ink);
    white-space: nowrap;
  }
  .headline-script {
    position: absolute;
    left: 200px;
    top: 82px;
    margin: 0;
    font-family: "Great Vibes", cursive;
    font-weight: 400;
    font-size: 112px;
    line-height: 1;
    letter-spacing: -2px;
    color: var(--ink);
    text-shadow: 3px 4px 4px rgba(0, 0, 0, 0.35);
    white-space: nowrap;
  }
  .tagline {
    position: absolute;
    left: 84px;
    top: 213px;
    width: 532px;
    margin: 0;
    text-align: center;
    font-family: "Cinzel", serif;
    font-weight: 600;
    font-size: 13.4px;
    letter-spacing: 0.2px;
    color: var(--ink-soft);
    white-space: nowrap;
  }
  .cta {
    position: absolute;
    left: 199px;
    top: 281px;
    width: 291px;
    height: 33px;
    line-height: 34px;
    background: var(--button-fill);
    font-family: "Arimo", sans-serif;
    font-size: 19px;
    letter-spacing: 1px;
    color: var(--ink);
    text-decoration: none;
    text-align: center;
  }
</style>
</head>
<body>
  <section class="banner">
    <svg class="banner__art" viewBox="0 0 1200 356" aria-hidden="false">
      <defs>
        <linearGradient id="backdrop-fill" x1="0" y1="0" x2="0" y2="1">
          <stop offset="0" stop-color="var(--backdrop-mid)"/>
          <stop offset="0.55" stop-color="var(--backdrop-light)"/>
          <stop offset="1" stop-color="var(--backdrop-dark)"/>
        </linearGradient>
        <linearGradient id="room-fill" x1="0" y1="0" x2="1" y2="0">
          <stop offset="0" stop-color="var(--room-dark)"/>
          <stop offset="0.35" stop-color="var(--room-mid)"/>
          <stop offset="0.7" stop-color="var(--room-light)"/>
          <stop offset="1" stop-color="var(--room-dark)"/>
        </linearGradient>
        <path id="heart" d="M0 -18 C -10 -38 -42 -34 -42 -8 C -42 14 -16 30 0 46 C 16 30 42 14 42 -8 C 42 -34 10 -38 0 -18 Z"/>
      </defs>

      <g role="img" aria-label="Softly faded photo of a mirrored dresser with lamp and decor">
        <rect width="1200" height="356" fill="url(#backdrop-fill)"/>
      </g>
      <rect class="maroon-veil" width="1200" height="356" fill="var(--maroon-veil)"/>

      <g class="faded-hearts" fill="var(--heart-tint)">
        <use href="#heart" transform="translate(330 170) scale(3.4)" opacity="0.13"/>
        <use href="#heart" transform="translate(60 70) scale(0.9) rotate(-14)" opacity="0.18"/>
        <use href="#heart" transform="translate(620 80) scale(0.7) rotate(12)" opacity="0.16"/>
        <use href="#heart" transform="translate(75 300) scale(0.6) rotate(10)" opacity="0.15"/>
        <use href="#heart" transform="translate(640 300) scale(0.5) rotate(-8)" opacity="0.15"/>
      </g>

      <g role="img" aria-label="Photo of a bedroom with upholstered bed, cushions, fur throw and mirrored bedside tables">
        <path d="M790 0 C 700 110, 610 220, 612 356 L 1200 356 L 1200 0 Z" fill="url(#room-fill)"/>
      </g>
      <path class="curve-edge" d="M790 0 C 700 110, 610 220, 612 356" fill="none" stroke="var(--curve-edge)" stroke-width="3"/>
    </svg>

    <div class="banner__content">
      <h1 class="headline-top">FIND A LOOK YOU</h1>
      <p class="headline-script">LOVE</p>
      <p class="tagline">Lorem ipsum not sure what the rest of this&nbsp; will say at the moment</p>
      <a class="cta" href="#">SHOP BEDROOMS</a>
    </div>
  </section>
</body>
</html>
```